Beer Can Labels Graphic Design

We need beer can label ideas for 4 different types of beer that we are producing. The 4 names and info required for each beer are as follows:

1. LHTRA. 6.0% ABV. 40 IBU. Strong Ale / Ale Forte. Indian Pale Ale

2. Wendmar Orange. 5.0% ABV. 10 IBU. Ale / Ale. Belgian Witbier. Brewed with Citrus peels and coriander

3. Larkfell Pale Ale 5.2% ABV. 30 IBU. Ale / Biere. Honey Rye Ale

4. Tussock Bay 3.2% ABV. 13 IBU. Light Ale / Ale Leger. Brown Ale

We would like to include our brewery name/logo "Hollowmere Brewing Company" on each of the can lables.

A bit of background:

LHTRA is an acronym of our company name with a bit of play on the local school "Hollowmere Tutorial Academy" which most locals enjoy as their is some humor in a beer named after a bible school.

The last 3 names are after each of the communities that each of the 3 owners grew up at. Wendmar, Larkfell and Tussock.

Wendmar is recognized by a large grain elevator witin the area.

Larkfell is recognized by a creek and ball diamonds.

Tussock is recognized by the dunsley ferry, badlands/hoodos.

One thing each community has in common is the fact that all 3 are farming communities.

We are packaging utilizing standard 355ml cans so the graphic design must fit on a 7.375" x 3.125".

I will attach our logo as well as some of our current ideas/graphics for reference or use.

Target Market(s)

Beer Drinkers

Industry/Entity Type

Brewery

Requirements
Must have
• Beer names in color and required info (ie alcohol content and beer in english and french)
• Company name/logo
Nice to have
• A section which can be utilized to insert a brief story with each beer.
• Scale to define beer type on 3 items. Malt, hop and color
• Something consistent from beer to beer so that it can be easily modified for new beers we develop.
• Possibly a picture faded in the background or our company logo.
Should not have
• Too busy or too much going on.

```html
<!DOCTYPE html>
<html lang="en">
<head>
<meta charset="UTF-8">
<title>Hollowmere Brewing Company – Tussock Bay Brown Ale</title>
<link rel="stylesheet" href="https://fonts.googleapis.com/css2?family=Bebas+Neue&display=swap">
<style>
  :root {
    --backdrop: #e9ebed;
    --label-charcoal: #2a2b2d;
    --label-charcoal-light: #3a3b3e;
    --badlands-red: #8b4a4d;
    --title-red: #6f2428;
    --ink-white: #f4f4f4;
    --ink-pink: #f3dcdc;
  }
  * { margin: 0; padding: 0; box-sizing: border-box; }
  html, body {
    width: 1200px;
    height: 900px;
    overflow: hidden;
    background: var(--backdrop);
    font-family: "Bebas Neue", "Oswald", sans-serif;
  }
  .canvas {
    position: relative;
    width: 1200px;
    height: 900px;
  }
  .can-label {
    position: absolute;
    left: 445px;
    top: 70px;
    width: 310px;
    height: 720px;
    background: linear-gradient(90deg, var(--label-charcoal) 0%, var(--label-charcoal-light) 50%, var(--label-charcoal) 100%);
    overflow: hidden;
  }
  .brewery-name {
    position: absolute;
    top: 225px;
    left: 0;
    width: 100%;
    text-align: center;
    color: var(--ink-white);
    line-height: 0.95;
  }
  .brewery-name .wordmark {
    display: block;
    font-size: 70px;
    letter-spacing: 1px;
  }
  .brewery-name .subline {
    display: block;
    font-size: 38px;
    letter-spacing: 0.5px;
    margin-top: 6px;
  }
  .beer-title {
    position: absolute;
    top: 418px;
    left: 0;
    width: 100%;
    text-align: center;
    color: var(--title-red);
    font-size: 62px;
    letter-spacing: 1px;
    line-height: 1;
  }
  .beer-style {
    position: absolute;
    top: 485px;
    left: 0;
    width: 100%;
    text-align: center;
    color: var(--ink-white);
    font-size: 20px;
    letter-spacing: 0.5px;
  }
  .badlands-band {
    position: absolute;
    left: 0;
    top: 480px;
    width: 100%;
    height: 240px;
  }
  .badlands-band svg { display: block; width: 100%; height: 100%; }
  .beer-facts {
    position: absolute;
    top: 605px;
    left: 0;
    width: 100%;
    color: var(--ink-pink);
    text-align: center;
  }
  .beer-facts .stats {
    display: flex;
    justify-content: space-between;
    padding: 0 14px;
    font-size: 20px;
    letter-spacing: 0.3px;
  }
  .beer-facts .class-line {
    margin-top: 14px;
    font-size: 21px;
    letter-spacing: 0.3px;
  }
</style>
</head>
<body>
  <main class="canvas">
    <section class="can-label">
      <div class="badlands-band">
        <svg viewBox="0 0 310 240" preserveAspectRatio="none" role="img" aria-label="Badlands hoodoo skyline in red, rising from the band below the beer name">
          <rect x="0" y="60" width="310" height="180" fill="var(--badlands-red)"/>
        </svg>
      </div>

      <h1 class="brewery-name">
        <span class="wordmark">HOLLOWMERE</span>
        <span class="subline">BREWING COMPANY</span>
      </h1>

      <h2 class="beer-title">TUSSOCK BAY</h2>
      <p class="beer-style">BROWN ALE</p>

      <div class="beer-facts">
        <p class="stats">
          <span>3.2% ABV.</span>
          <span>13 IBU.</span>
          <span>12 FL OZ (355 ML)</span>
        </p>
        <p class="class-line">LIGHT ALE / ALE LEGER.</p>
      </div>
    </section>
  </main>
</body>
</html>
```